Book Cover Design KRT

Want a new book cover but want to use the same photo and change the sub name. This is for a brand called "Golden Rose Living". The book is called "Bare Floor, Full Power"

This is for a 8.5 * 11 book size

We really want to brand the Golden Rose Living

I've attached a sample of an old book cover, the photo I want used and the golden rose living logo
Updates

Requirements
Must have
• Must have the logo,

must have the book title. "Bare Floor, Full Power"

Must have "Featuring" The Golden Rose Living Fold Up Card Game"

On the back put the logo and Golden Rose Living Nutrition

must have the authors name "Dana Pellow" on the page

"The Sunrise Shape Guide"
Nice to have
• Golden Rose Living Presents:

the book title

```html
<!DOCTYPE html>
<html lang="en">
<head>
<meta charset="utf-8">
<title>Bare Floor, Full Power – Book Cover</title>
<link rel="stylesheet" href="https://fonts.googleapis.com/css2?family=Anton&family=Montserrat:wght@400;500;700&family=Oswald:wght@500;600&family=Pathway+Gothic+One&display=swap">
<style>
  :root {
    --bg: #4cc2a6;
    --ink: #000000;
    --paper: #ffffff;
    --mint: #7fd3c0;
    --frame: #e6e6e6;
  }
  * { box-sizing: border-box; margin: 0; padding: 0; }
  html, body { width: 1200px; height: 900px; overflow: hidden; }
  body { background: var(--bg); position: relative; font-family: "Montserrat", sans-serif; }

  .book { position: absolute; left: 168px; top: 120px; width: 864px; height: 660px; display: flex; }

  /* Back cover */
  .back-cover { width: 420px; height: 660px; background: var(--frame); position: relative; }
  .back-panel { position: absolute; inset: 26px; background: var(--ink); display: flex; flex-direction: column; align-items: center; }
  .brand-mark { margin-top: 74px; display: flex; align-items: center; gap: 10px; color: var(--paper); font-family: "Montserrat", sans-serif; font-weight: 500; font-size: 19px; letter-spacing: 2px; text-transform: uppercase; }
  .brand-mark .dot { width: 14px; height: 14px; border-radius: 50%; background: var(--paper); }
  .brand-sub { margin-top: 8px; color: var(--paper); font-size: 10px; letter-spacing: 4px; text-transform: uppercase; }
  .affirmations { list-style: none; margin-top: 42px; text-align: center; color: var(--paper); font-family: "Pathway Gothic One", sans-serif; font-size: 31px; line-height: 40px; text-transform: uppercase; }

  /* Spine */
  .spine { width: 24px; height: 660px; background: var(--ink); position: relative; color: var(--paper); }
  .spine-text { position: absolute; left: 50%; transform: translateX(-50%); writing-mode: vertical-rl; white-space: nowrap; }
  .spine-brand { top: 24px; font-size: 6px; letter-spacing: 1.5px; }
  .spine-title { top: 210px; font-family: "Montserrat", sans-serif; font-weight: 700; font-size: 11px; letter-spacing: 1px; }
  .spine-author { top: 520px; font-size: 7px; letter-spacing: 2px; }

  /* Front cover */
  .front-cover { width: 420px; height: 660px; background: var(--ink); position: relative; overflow: hidden; }
  .cover-photo { position: absolute; left: 56px; top: 0; width: 364px; height: 660px;
    background: radial-gradient(ellipse at 35% 38%, #5fae9c 0 22%, transparent 23%),
                radial-gradient(ellipse at 70% 45%, #4a3328 0 28%, #000 60%); }
  .ball-brand { position: absolute; left: 100px; top: 285px; display: flex; align-items: center; gap: 6px; color: var(--ink); font-size: 11px; font-weight: 500; letter-spacing: 1.5px; text-transform: uppercase; }
  .ball-brand .dot { width: 9px; height: 9px; border-radius: 50%; background: var(--ink); }
  .series { position: absolute; left: 22px; top: 36px; color: var(--paper); font-size: 15px; line-height: 19px; text-transform: uppercase; }
  .series strong { font-weight: 700; }
  .rule { position: absolute; height: 2px; background: var(--mint); }
  .rule-series { left: 22px; top: 102px; width: 130px; }
  .author { position: absolute; left: 22px; top: 112px; color: var(--mint); font-size: 20px; }
  .title { position: absolute; left: 18px; top: 326px; color: var(--paper); font-family: "Anton", sans-serif; font-size: 76px; line-height: 96px; text-transform: uppercase; letter-spacing: 1px; }
  .rule-feature-top { left: 22px; top: 535px; width: 180px; }
  .rule-feature-bottom { left: 22px; top: 622px; width: 185px; }
  .featuring { position: absolute; left: 22px; top: 542px; font-family: "Oswald", sans-serif; text-transform: uppercase; line-height: 1.15; }
  .featuring .label { color: var(--mint); font-size: 16px; font-weight: 600; }
  .featuring .line { color: var(--paper); font-size: 13px; font-weight: 500; }
  .featuring .game { color: var(--mint); font-size: 19px; font-weight: 600; }
</style>
</head>
<body>
  <div class="book">
    <section class="back-cover" role="img" aria-label="Back cover with patterned border around a black panel">
      <div class="back-panel">
        <div class="brand-mark"><span class="dot"></span>Golden Rose Living</div>
        <div class="brand-sub">Nutrition</div>
        <ul class="affirmations">
          <li>I crush my goals</li>
          <li>I persever</li>
          <li>I take decsive action</li>
          <li>I am deliberate</li>
          <li>I hold my head high</li>
          <li>I don't quit</li>
          <li>I am formidable</li>
          <li>I am secure</li>
          <li>I am motivated</li>
          <li>I am loved</li>
        </ul>
      </div>
    </section>

    <section class="spine">
      <span class="spine-text spine-brand">GOLDEN ROSE LIVING</span>
      <span class="spine-text spine-title">BARE FLOOR, FULL POWER</span>
      <span class="spine-text spine-author">DANA PELLOW</span>
    </section>

    <section class="front-cover">
      <div class="cover-photo" role="img" aria-label="Photo of the author in workout wear resting an arm on a mint exercise ball"></div>
      <div class="ball-brand"><span class="dot"></span>Golden Rose Living</div>
      <p class="series">Your<br><strong>Sunrise Shape</strong><br>Guide</p>
      <div class="rule rule-series"></div>
      <p class="author">by DANA PELLOW</p>
      <h1 class="title">Bare Floor<br>Full Power</h1>
      <div class="rule rule-feature-top"></div>
      <div class="featuring">
        <div class="label">Featuring:</div>
        <div class="line">“The Golden Rose Living</div>
        <div class="game">Fold Up Card Game”</div>
      </div>
      <div class="rule rule-feature-bottom"></div>
    </section>
  </div>
</body>
</html>
```